Roofing web site brvt roofing

Look at some of our competitors web page we like something similar with NYC roofing
https://www.dellowtopcoat.example/
Maybe a skyline picture of nyc at the home page with a picture of flat roofing installation

Target Market(s)

Commercial and residential flat roofs

Industry/Entity Type

Flat Roofing industry

Coding

Coded - Design and coding required

Number of Pages Required

2 page

Font styles to use
Decorative
Script

Colors

Designer to choose colors to be used in the design.

Requirements
Must have
• At BRVT Roofing, we are a trusted and reputable roofing company specializing in new construction flat roof installation and repair. With years of experience in the industry, we take pride in providing exceptional roofing solutions to our valued clients. Our team of highly skilled and dedicated roofing professionals understands the unique challenges and requirements of new construction projects. We work closely with builders, contractors, and architects to design and install flat roofs that meet the specific needs of each project. From commercial buildings to residential complexes, we have the expertise to deliver reliable and durable roofing solutions. When it comes to flat roof repairs, we are your go-to experts. Our experienced technicians conduct thorough inspections to identify the root cause of any issues your roof may be experiencing. We utilize the latest industry techniques and high-quality materials to efficiently repair your flat roof, ensuring its integrity and longevity. At BRVT Roofing, we prioritize customer satisfaction above all else. We believe in building strong relationships with our clients by providing exceptional craftsmanship and outstanding customer service. Our team is dedicated to delivering projects on time, within budget, and to the highest standards of quality. We understand that a well-maintained roof is essential for protecting your property and ensuring the safety of its occupants. That's why we use only the best materials and employ skilled professionals who are trained in the latest roofing practices. Our commitment to excellence is evident in every project we undertake. As a fully licensed and insured roofing company, we prioritize safety and adhere to industry regulations and best practices. We take every precaution to create a safe working environment for our team and minimize any disruptions to your daily routine. When you choose BRVT Roofing, you can trust that you are working with a reliable and reputable company that will deliver exceptional results. We are committed to exceeding your expectations and providing you with a roof that is built to last. Contact us today for all your new construction flat roof installation and repair needs.
Nice to have
• NYC skyline background with commercial roofing pictures of torching roofing

```html
<!DOCTYPE html>
<html lang="en">
<head>
<meta charset="utf-8">
<title>BRVT Construction Roofing</title>
<link href="https://fonts.googleapis.com/css2?family=Roboto+Condensed:wght@400;700&family=Montserrat:wght@400;500;600;700&family=Great+Vibes&display=swap" rel="stylesheet">
<style>
:root{
  --orange:#f26a2e;
  --orange-dark:#e2551c;
  --ink:#1b1b1b;
  --dark:#222325;
  --text:#333;
  --muted:#6a6a6a;
  --line:#cfcfcf;
  --white:#fff;
}
*{margin:0;padding:0;box-sizing:border-box}
html,body{width:1200px;height:3984px;overflow:hidden;background:var(--white)}
body{position:relative;font-family:'Montserrat',sans-serif;color:var(--text)}
.abs{position:absolute}
.cond{font-family:'Roboto Condensed',sans-serif;font-weight:700;text-transform:uppercase}
.accent{color:var(--orange)}
.btn{position:absolute;display:flex;align-items:center;justify-content:center;font-family:'Roboto Condensed',sans-serif;font-weight:700;text-transform:uppercase;letter-spacing:.5px}
.btn-solid{background:linear-gradient(#f7783c,var(--orange-dark));color:#fff}
.btn-outline{border:2px solid var(--orange);color:var(--orange);background:#fff}

/* header */
.site-header{top:0;left:0;width:1200px;height:93px}
.social{top:24px;left:135px;display:flex;gap:10px}
.social span{width:38px;height:38px;border-radius:50%;background:var(--ink);display:block}
.social span:first-child{background:var(--orange)}
.brand-name{top:14px;left:0;width:1178px;text-align:center;font-size:29px;line-height:31px;color:var(--ink)}
.phone-badge{top:22px;left:862px;width:236px;height:42px;background:var(--orange);clip-path:polygon(0 0,100% 0,92% 100%,0 100%);border-radius:21px 0 0 21px}
.phone-badge .ico{position:absolute;left:2px;top:2px;width:38px;height:38px;border-radius:50%;background:var(--ink);display:flex;align-items:center;justify-content:center}
.phone-badge b{position:absolute;left:54px;top:9px;color:#fff;font-size:19px;font-weight:600}

.main-nav{top:93px;left:0;width:1200px;height:54px;background:var(--ink)}
.main-nav a{position:absolute;top:0;height:54px;line-height:54px;color:#fff;font-size:16px;font-weight:700;text-decoration:none}
.main-nav a.active{border-bottom:3px solid var(--orange)}

/* hero */
.hero{top:147px;left:0;width:1200px;height:592px;background:linear-gradient(180deg,#8dbbe0 0%,#bcd6ea 45%,#d9d8d2 70%,#6c6a66 100%)}
.hero-worker{top:147px;left:0;width:560px;height:592px;background:linear-gradient(100deg,#3c3f46,#6b6a68 60%,rgba(120,120,120,0))}
.hero-script{top:212px;left:0;width:1200px;text-align:center;font-family:'Great Vibes',cursive;font-size:42px;color:var(--orange)}
.hero-title{top:278px;left:0;width:1200px;text-align:center;font-family:'Roboto Condensed',sans-serif;font-weight:400;font-size:50px;line-height:50px;color:#e8eaee;-webkit-text-stroke:1.5px #3a3c44;letter-spacing:1px}
.scroll-chev{top:570px;left:580px}

.feature-bar{top:703px;height:147px;display:flex;align-items:center;padding-left:32px;gap:16px;color:#fff}
.feature-bar h3{font-size:20px;margin-bottom:4px}
.feature-bar p{font-size:12px;line-height:19px;color:#ffe3d6}
.feature-bar.orange{background:var(--orange)}
.feature-bar.dark{background:var(--dark);top:685px;height:165px}
.feature-bar.dark p{color:#cfcfcf}

/* about */
.about{top:850px;left:0;width:1200px;height:514px;background:linear-gradient(180deg,#fff 0%,#fff 62%,#e8edf2 80%,#c9d0d8 100%)}
.about-frame{top:971px;left:164px;width:864px;height:270px;border:3px solid var(--line)}
.eyebrow{font-family:'Roboto Condensed',sans-serif;font-size:20px;color:var(--orange);letter-spacing:1px;text-transform:uppercase}
.about-eyebrow{top:908px;left:0;width:1200px;text-align:center}
.about-title{top:940px;left:390px;width:420px;text-align:center;background:#fff;font-size:42px;line-height:44px;color:var(--ink)}
.about-text{top:1046px;left:230px;width:740px;text-align:center;font-size:17px;line-height:27px;color:#2b2b2b}

/* services */
.section-title{left:0;width:1200px;text-align:center;font-size:42px;color:var(--ink)}
.title-rule{height:2px;background:var(--orange);width:110px}
.title-rule::after{content:"";position:absolute;left:50%;top:-2px;width:6px;height:6px;margin-left:-3px;border-radius:50%;background:var(--orange)}
.svc-card{top:1555px;height:277px;border:2px solid var(--line);background:#fff;text-align:center}
.svc-card.featured{border-color:var(--orange)}
.svc-icon{position:absolute;top:-48px;left:50%;margin-left:-48px;width:96px;height:96px;border-radius:50%;background:var(--orange);display:flex;align-items:center;justify-content:center}
.featured .svc-icon{background:var(--ink)}
.svc-card h4{margin-top:70px;font-size:20px;line-height:22px;color:var(--ink)}
.svc-card p{margin:12px auto 0;width:250px;font-size:12px;line-height:19.5px;color:#444}
.svc-card .btn{left:50%;bottom:28px;width:146px;height:38px;margin-left:-73px;font-size:13px}

/* why */
.why{top:1902px;left:0;width:1200px;height:578px;background:linear-gradient(90deg,#1c1d20,#2d2f33)}
.why-photo{top:1902px;left:0;width:1200px;height:578px;background:linear-gradient(135deg,#6e88a8 0%,#a6b4c6 40%,#d8dde3 75%,#eef0f2 100%);clip-path:polygon(773px 0,1200px 0,1200px 578px,448px 578px)}
.why-stripe{top:1902px;left:0;width:1200px;height:578px}
.why-eyebrow{top:1996px;left:125px}
.why-title{top:2024px;left:125px;font-size:42px;color:#fff}
.why-text{top:2100px;left:125px;width:480px;font-size:13.5px;line-height:19.5px;color:#e8e8e8}
.why-list{top:2192px;left:128px;list-style:none}
.why-list li{height:34.5px;display:flex;align-items:center;gap:10px;color:#fff;font-size:15px;font-weight:700}

/* gallery */
.gallery-item{top:2656px;height:274px}
.dots{top:2964px;left:532px;display:flex;gap:18px}
.dots i{width:38px;height:3px;background:var(--ink);display:block}
.dots i.on{background:var(--orange)}

/* contact */
.contact{top:2930px;left:0;width:1200px;height:638px;background:linear-gradient(180deg,#fff 0%,#fff 55%,#e4e8ec 75%,#b9c0c8 100%)}
.contact-eyebrow{top:3040px;left:137px}
.contact-title{top:3072px;left:136px;font-size:42px;color:var(--ink)}
.contact-rule{top:3130px;left:136px}
.contact-item{left:136px;display:flex;align-items:center;gap:20px;font-size:19px;line-height:24px;color:#222}
.contact-item .ico{width:60px;height:60px;border-radius:50%;background:var(--orange);display:flex;align-items:center;justify-content:center;flex:none}
.quote-box{top:3036px;left:555px;width:547px;height:388px;background:var(--orange);border-radius:6px;box-shadow:0 8px 24px rgba(0,0,0,.12)}
.quote-title{top:3077px;left:603px;font-size:30px;color:#fff}
.field{background:#fff;font-size:13px;color:#333;padding:12px 18px}
.send-btn{top:3335px;left:603px;width:190px;height:42px;background:var(--ink);color:#fff;font-size:16px}

/* footer */
.site-footer{top:3568px;left:0;width:1200px;height:416px;background:var(--ink)}
.footer-div{top:3568px;width:1px;height:336px;background:#3a3a3a}
.footer-head{top:3632px;font-size:21px;color:#fff;border-left:3px solid var(--orange);padding-left:24px;line-height:26px}
.footer-brand{top:3630px;left:108px;font-family:'Roboto Condensed',sans-serif;font-weight:700;font-size:28px;line-height:36px;color:#fff}
.footer-social{top:3726px;left:112px;display:flex;gap:16px}
.footer-social span{width:36px;height:36px;border-radius:50%;background:#3a3a3a;display:block}
.footer-social span:first-child{background:var(--orange)}
.footer-links{top:3674px;left:404px;list-style:none}
.footer-links li{font-size:12px;line-height:26px;color:#ddd}
.footer-contact{left:618px;display:flex;gap:12px;align-items:center;font-size:12px;line-height:16px;color:#ddd}
.copyright{top:3904px;left:0;width:1200px;height:80px;border-top:1px solid #333;text-align:center;line-height:80px;font-size:12px;color:#bbb}
</style>
</head>
<body>

<!-- header -->
<header class="abs site-header">
  <div class="abs social" aria-label="Social profiles"><span></span><span></span><span></span></div>
  <div class="abs brand-name cond">BRVT Construction<br>Roofing</div>
  <div class="abs phone-badge">
    <div class="ico"><svg width="18" height="18" viewBox="0 0 24 24" fill="#fff"><path d="M6.6 10.8a15.1 15.1 0 006.6 6.6l2.2-2.2c.3-.3.7-.4 1-.2 1.1.4 2.3.6 3.6.6.6 0 1 .4 1 1V20c0 .6-.4 1-1 1A17 17 0 013 4c0-.6.4-1 1-1h3.5c.6 0 1 .4 1 1 0 1.3.2 2.5.6 3.6.1.3 0 .7-.2 1z"/></svg></div>
    <b>(555) 214 3380</b>
  </div>
</header>
<nav class="abs main-nav">
  <a class="active" href="#" style="left:159px;width:96px;text-align:center">HOME</a>
  <a href="#" style="left:324px">ABOUT US</a>
  <a href="#" style="left:509px">SERVICES <svg width="14" height="10" viewBox="0 0 14 10"><path d="M2 2l5 5 5-5" stroke="#fff" stroke-width="2" fill="none"/></svg></a>
  <a href="#" style="left:684px">PHOTO GALLERY</a>
  <a href="#" style="left:925px">CONTACT US</a>
</nav>

<!-- hero -->
<section class="abs hero" role="img" aria-label="City skyline with high-rise towers under a blue sky"></section>
<div class="abs hero-worker" role="img" aria-label="Roofer in a hard hat torching a flat roof membrane"></div>
<div class="abs hero-script">BRVT Construction Roofing</div>
<h1 class="abs hero-title">PROFESSIONAL &amp; AFFORDABLE<br>ROOFING SERVICES.</h1>
<a class="btn btn-solid" style="top:390px;left:512px;width:178px;height:48px;font-size:17px">CONTACT US &#8250;</a>
<svg class="abs scroll-chev" width="40" height="24" viewBox="0 0 40 24"><path d="M6 6l14 12L34 6" stroke="#fff" stroke-width="3" fill="none" opacity=".8"/></svg>

<div class="abs feature-bar orange" style="left:113px;width:323px">
  <svg width="50" height="46" viewBox="0 0 50 46" fill="none" stroke="#fff" stroke-width="2"><path d="M4 22L25 5l21 17M10 18v24h30V18M20 42V28h10v14"/></svg>
  <div><h3 class="cond">Roof Leak Repair</h3><p>Lorem ipsum dolor sit amet consec-<br>tetur adipiscing elit sed d</p></div>
</div>
<div class="abs feature-bar dark" style="left:436px;width:312px;">
  <svg width="50" height="50" viewBox="0 0 50 50" fill="none" stroke="#fff" stroke-width="2"><circle cx="25" cy="16" r="9"/><path d="M12 44c2-10 8-14 13-14s11 4 13 14"/><circle cx="12" cy="36" r="5"/></svg>
  <div><h3 class="cond">Flashing Services</h3><p>Lorem ipsum dolor sit amet con-<br>sectetur adipiscing elit sed d</p></div>
</div>
<div class="abs feature-bar orange" style="left:748px;width:325px;padding-left:22px">
  <svg width="50" height="44" viewBox="0 0 50 44" fill="none" stroke="#fff" stroke-width="2"><path d="M6 40l10-30h28L34 40zM11 25h28M21 10l-5 30M31 10l-5 30"/></svg>
  <div><h3 class="cond">Waterproofing Experts</h3><p>Lorem ipsum dolor sit amet consec-<br>tetur adipiscing elit sed d</p></div>
</div>

<!-- about -->
<section class="abs about"></section>
<div class="abs about-frame"></div>
<div class="abs about-eyebrow eyebrow">Who We Are</div>
<h2 class="abs about-title cond">BRVT Construction<br><span class="accent">Roofing</span></h2>
<p class="abs about-text">At BRVT Roofing, we are a trusted and reputable roofing company specializing in new construction flat roof installation and repair. With years of experience in the industry, we take pride in providing exceptional roofing solutions to our valued clients. Our team of highly skilled and dedicated roofing professionals understands the unique challenges and requirements of new construction projects.</p>
<a class="btn btn-solid" style="top:1214px;left:497px;width:195px;height:52px;font-size:17px">LEARN MORE &#8250;</a>

<!-- services -->
<h2 class="abs section-title cond" style="top:1414px">Services <span class="accent">Provide</span></h2>
<div class="abs title-rule" style="top:1478px;left:545px"></div>

<div class="abs svc-card" style="left:110px;width:318px">
  <div class="svc-icon"><svg width="50" height="50" viewBox="0 0 50 50" fill="none" stroke="#fff" stroke-width="2"><circle cx="25" cy="17" r="8"/><path d="M15 12h20M12 46c1-11 6-15 13-15s12 4 13 15"/></svg></div>
  <h4 class="cond">Reliable Roofing<br>Professionals</h4>
  <p>As specialists in residential and commercial roofing services, we are dedicated to providing customer service that is second to none.</p>
  <a class="btn btn-outline">LEARN MORE &#8250;</a>
</div>
<div class="abs svc-card featured" style="left:444px;width:317px">
  <div class="svc-icon"><svg width="54" height="46" viewBox="0 0 54 46" fill="none" stroke="#fff" stroke-width="2"><path d="M6 10h42v26H6zM6 18h42M6 27h42M16 10v26M27 10v26M38 10v26M4 42c8-4 14 4 23 0s15 4 23 0"/></svg></div>
  <h4 class="cond">Individualized<br>Roofing Options</h4>
  <p>As specialists in residential and commercial roofing services, we are dedicated to providing customer service that is second to none.</p>
  <a class="btn btn-solid">LEARN MORE &#8250;</a>
</div>
<div class="abs svc-card" style="left:778px;width:318px">
  <div class="svc-icon"><svg width="46" height="50" viewBox="0 0 46 50" fill="none" stroke="#fff" stroke-width="2"><path d="M23 4l17 6v14c0 11-8 19-17 22C14 43 6 35 6 24V10z"/><path d="M15 26h5v10h-5zM20 34h9c2 0 3-1 3-3l1-7c0-2-1-3-3-3h-5l1-6c0-2-3-2-3 0l-3 7"/></svg></div>
  <h4 class="cond">Satisfaction<br>Guaranteed</h4>
  <p>As specialists in residential and commercial roofing services, we are dedicated to providing customer service that is second to none.</p>
  <a class="btn btn-outline">LEARN MORE &#8250;</a>
</div>

<!-- why choose -->
<section class="abs why"></section>
<div class="abs why-photo" role="img" aria-label="Roofer in a yellow hard hat torching a flat roof"></div>
<svg class="abs why-stripe" width="1200" height="578" viewBox="0 0 1200 578"><path d="M711 105L479 498" stroke="#f26a2e" stroke-width="12"/></svg>
<div class="abs why-eyebrow eyebrow">Why We Are</div>
<h2 class="abs why-title cond">Why Choose <span class="accent">Us</span></h2>
<p class="abs why-text">We work closely with builders, contractors, and architects to design and install flat roofs that meet the specific needs of each project. From commercial buildings to residential complexes, we have the expertise to deliver reliable and durable roofing solutions.</p>
<ul class="abs why-list">
  <li><svg width="20" height="16" viewBox="0 0 20 16"><path d="M2 8l6 6L18 2" stroke="#f26a2e" stroke-width="3" fill="none"/></svg>Licensed, Bonded &amp; Insured</li>
  <li><svg width="20" height="16" viewBox="0 0 20 16"><path d="M2 8l6 6L18 2" stroke="#f26a2e" stroke-width="3" fill="none"/></svg>Reliable &amp; Experienced Professional</li>
  <li><svg width="20" height="16" viewBox="0 0 20 16"><path d="M2 8l6 6L18 2" stroke="#f26a2e" stroke-width="3" fill="none"/></svg>Lead Safe Certified</li>
  <li><svg width="20" height="16" viewBox="0 0 20 16"><path d="M2 8l6 6L18 2" stroke="#f26a2e" stroke-width="3" fill="none"/></svg>24/7 Emergency Response</li>
  <li><svg width="20" height="16" viewBox="0 0 20 16"><path d="M2 8l6 6L18 2" stroke="#f26a2e" stroke-width="3" fill="none"/></svg>Top Rated Local Business</li>
</ul>

<!-- gallery -->
<div class="abs eyebrow" style="top:2536px;left:0;width:1186px;text-align:center">Our Gallery</div>
<h2 class="abs section-title cond" style="top:2560px;width:1186px">Project Gallery</h2>
<div class="abs title-rule" style="top:2621px;left:538px"></div>
<div class="abs gallery-item" style="left:0;width:297px;background:linear-gradient(150deg,#9fb6cc,#e9ecee 60%,#7c8790)" role="img" aria-label="White rain gutter along a roof edge"></div>
<div class="abs gallery-item" style="left:300px;width:298px;background:linear-gradient(160deg,#b4532c,#d9754a 55%,#8c3f22)" role="img" aria-label="Worker pressure washing a tiled roof with a skylight"></div>
<div class="abs gallery-item" style="left:601px;width:298px;background:linear-gradient(150deg,#8a949c,#5e666d 60%,#3b4045)" role="img" aria-label="Nail gun fastening shingles on a roof"></div>
<div class="abs gallery-item" style="left:903px;width:297px;background:linear-gradient(160deg,#9c8f7e,#c9b8a0 50%,#6e5a46)" role="img" aria-label="Roof insulation between timber rafters"></div>
<div class="abs dots"><i></i><i class="on"></i><i></i></div>

<!-- contact -->
<section class="abs contact"></section>
<div class="abs contact-eyebrow eyebrow">Get in Touch</div>
<h2 class="abs contact-title cond">Contact <span class="accent">Us</span></h2>
<div class="abs title-rule contact-rule"></div>
<div class="abs contact-item" style="top:3164px">
  <div class="ico"><svg width="22" height="28" viewBox="0 0 22 28" fill="#fff"><path d="M11 0a11 11 0 00-11 11c0 8 11 17 11 17s11-9 11-17A11 11 0 0011 0zm0 15a4 4 0 110-8 4 4 0 010 8z"/></svg></div>
  <div>48 Harbor Lane Street,<br>10021 New York NY</div>
</div>
<div class="abs contact-item" style="top:3257px">
  <div class="ico"><svg width="24" height="24" viewBox="0 0 24 24" fill="#fff"><path d="M6.6 10.8a15.1 15.1 0 006.6 6.6l2.2-2.2c.3-.3.7-.4 1-.2 1.1.4 2.3.6 3.6.6.6 0 1 .4 1 1V20c0 .6-.4 1-1 1A17 17 0 013 4c0-.6.4-1 1-1h3.5c.6 0 1 .4 1 1 0 1.3.2 2.5.6 3.6.1.3 0 .7-.2 1z"/></svg></div>
  <div>Phone Number<br>555-214-3380</div>
</div>
<div class="abs contact-item" style="top:3350px">
  <div class="ico"><svg width="28" height="28" viewBox="0 0 28 28" fill="none" stroke="#fff" stroke-width="3"><circle cx="14" cy="14" r="11"/><path d="M14 7v7l5 3"/></svg></div>
  <div>Monday - Friday: 8am - 5pm<br>Saturday - Sunday: 8am-12</div>
</div>

<div class="abs quote-box"></div>
<h3 class="abs quote-title cond">Request a Quote</h3>
<div class="abs field" style="top:3129px;left:601px;width:225px;height:40px">First Name</div>
<div class="abs field" style="top:3129px;left:835px;width:227px;height:40px">Last Name</div>
<div class="abs field" style="top:3183px;left:601px;width:225px;height:40px">Phone</div>
<div class="abs field" style="top:3183px;left:835px;width:227px;height:40px">Email address</div>
<div class="abs field" style="top:3237px;left:601px;width:461px;height:84px">Leave Message</div>
<a class="btn send-btn">SEND MESSAGE</a>

<!-- footer -->
<footer class="abs site-footer"></footer>
<div class="abs footer-div" style="left:371px"></div>
<div class="abs footer-div" style="left:581px"></div>
<div class="abs footer-div" style="left:857px"></div>
<div class="abs footer-brand">BRVT Construction<br>Roofing</div>
<div class="abs footer-social"><span></span><span></span><span></span></div>
<h4 class="abs footer-head cond" style="left:372px">Navigation</h4>
<ul class="abs footer-links"><li>Home</li><li>About Us</li><li>Services</li><li>Gallery</li><li>Contact Us</li></ul>
<h4 class="abs footer-head cond" style="left:583px">Contact Us</h4>
<div class="abs footer-contact" style="top:3678px"><svg width="14" height="18" viewBox="0 0 22 28" fill="#fff"><path d="M11 0a11 11 0 00-11 11c0 8 11 17 11 17s11-9 11-17A11 11 0 0011 0zm0 15a4 4 0 110-8 4 4 0 010 8z"/></svg>48 Harbor Lane Street</div>
<div class="abs footer-contact" style="top:3720px"><svg width="16" height="16" viewBox="0 0 24 24" fill="#fff"><path d="M6.6 10.8a15.1 15.1 0 006.6 6.6l2.2-2.2c.3-.3.7-.4 1-.2 1.1.4 2.3.6 3.6.6.6 0 1 .4 1 1V20c0 .6-.4 1-1 1A17 17 0 013 4c0-.6.4-1 1-1h3.5c.6 0 1 .4 1 1 0 1.3.2 2.5.6 3.6.1.3 0 .7-.2 1z"/></svg>555-214-3380</div>
<div class="abs footer-contact" style="top:3760px"><svg width="18" height="18" viewBox="0 0 28 28" fill="none" stroke="#fff" stroke-width="3"><circle cx="14" cy="14" r="11"/><path d="M14 7v7l5 3"/></svg><span>Monday - Friday: 8am - 5pm<br>Saturday - Sunday: 8am-12</span></div>
<h4 class="abs footer-head cond" style="left:858px">Newsletter Sign Up</h4>
<div class="abs field" style="top:3680px;left:883px;width:218px;height:32px;padding:8px 12px;font-size:11px">Email address*</div>
<a class="btn btn-solid" style="top:3721px;left:883px;width:218px;height:34px;font-size:13px">SUBSCRIBE</a>
<div class="abs copyright">Copyright &copy; 2024 BRVT Construction Roofing - All Rights Reserved.</div>

</body>
</html>
```